Medical Staffing agency

I need a logo design that can stand along and become a brand. I'm not too particular of the design. Want something catchy and hopefully related to the Health field. Not important though. An example of what I'm looking for is the Steel Harbor Logo, or the Solvent Logo. Something that can become a brand without having to say the brand name. A bit about my company, I hire medical staff, and contract with other companies to provide anywhere from short term to long term employees. But that is expanding to more than just that.

Industry/Entity Type

Medical

Contact Information for Business Card

Meridel Rehab Services
Lucas Brenner, CEO
842 Pinecroft Ave
Suite 71
Clovis, CA 93612

```html
<!DOCTYPE html>
<html lang="en">
<head>
<meta charset="utf-8">
<title>Meridel Rehab Services – Business Card</title>
<link rel="stylesheet" href="https://fonts.googleapis.com/css2?family=Cinzel:wght@400;700&display=swap">
<style>
  :root {
    --bg: #e9ebee;
    --card: #ffffff;
    --blue-deep: #1f3fa8;
    --blue-mid: #1a73d9;
    --blue-bright: #12a6ee;
    --name-blue: #3a3f9e;
    --ink: #3b3b3b;
    --rule-grey: #9a9ea4;
  }
  * { margin: 0; padding: 0; box-sizing: border-box; }
  html, body { width: 1200px; height: 901px; overflow: hidden; }
  body {
    background: var(--bg);
    font-family: "Cinzel", serif;
    position: relative;
  }
  .card {
    position: absolute;
    left: 150px; top: 193px;
    width: 900px; height: 514px;
    background: var(--card);
    border-radius: 42px;
    overflow: hidden;
    box-shadow: 0 10px 30px rgba(0,0,0,0.18);
  }
  .card__swoosh { position: absolute; inset: 0; }
  .brand {
    position: absolute;
    left: 70px; top: 172px;
    display: flex; align-items: center; gap: 16px;
  }
  .brand__mark {
    width: 22px; height: 22px; border-radius: 50%;
    background: var(--blue-mid);
  }
  .brand__name {
    font-weight: 700; font-size: 28px; color: var(--blue-deep);
    letter-spacing: 0.5px; line-height: 1.1;
  }
  .person {
    position: absolute; right: 60px; top: 95px; text-align: right;
  }
  .person__name { font-size: 28px; color: var(--name-blue); letter-spacing: 1px; line-height: 1.2; }
  .person__title { font-size: 18px; color: var(--ink); letter-spacing: 1px; margin-top: 2px; }
  .address {
    position: absolute; right: 60px; top: 185px; text-align: right;
    font-size: 16px; color: var(--ink); line-height: 1.4; letter-spacing: 0.5px;
  }
  .contacts {
    position: absolute; right: 52px; top: 262px; list-style: none; text-align: right;
    font-size: 15px; color: var(--ink); letter-spacing: 0.6px;
  }
  .contacts li { display: flex; justify-content: flex-end; align-items: center; gap: 10px; height: 22px; }
  .contacts svg { width: 14px; height: 14px; fill: var(--blue-deep); }
</style>
</head>
<body>
  <section class="card" aria-label="Business card front">
    <svg class="card__swoosh" viewBox="0 0 900 514" preserveAspectRatio="none" aria-hidden="true">
      <defs>
        <linearGradient id="band" x1="0" y1="0" x2="1" y2="0.4">
          <stop offset="0" stop-color="var(--blue-deep)"/>
          <stop offset="0.45" stop-color="var(--blue-bright)"/>
          <stop offset="1" stop-color="var(--blue-mid)"/>
        </linearGradient>
      </defs>
      <path d="M0 300 C 350 300, 650 410, 900 512 L 900 514 L 0 514 Z" fill="url(#band)"/>
      <path d="M0 290 C 350 286, 650 396, 900 498" fill="none" stroke="var(--rule-grey)" stroke-width="5"/>
    </svg>

    <div class="brand">
      <span class="brand__mark"></span>
      <span class="brand__name">Meridel Rehab<br>Services</span>
    </div>

    <div class="person">
      <p class="person__name">Lucas Brenner</p>
      <p class="person__title">CEO</p>
    </div>

    <p class="address">842 Pinecroft Ave<br>Suite 71, Clovis CA</p>

    <ul class="contacts">
      <li>559 014 2738 <svg viewBox="0 0 16 16"><path d="M3 1l3 3-2 2c1 2 3 4 5 5l2-2 3 3-2 3C7 15 1 9 0 3z"/></svg></li>
      <li>559 014 2739 <svg viewBox="0 0 16 16"><path d="M4 0h8v16H4zM5.5 2v10h5V2z" fill-rule="evenodd"/></svg></li>
      <li>559 014 2740 <svg viewBox="0 0 16 16"><path d="M2 5h12v11H2zM4 0h8v5H4z"/></svg></li>
      <li>lucas@meridelrehab.com <svg viewBox="0 0 16 16"><path d="M0 3h16v10H0zM1 4l7 5 7-5z" fill-rule="evenodd"/></svg></li>
      <li>www.meridelrehab.com <svg viewBox="0 0 16 16"><circle cx="8" cy="8" r="7" fill="none" stroke="var(--blue-deep)" stroke-width="1.5"/><path d="M1 8h14M8 1v14" stroke="var(--blue-deep)" stroke-width="1.2"/></svg></li>
    </ul>
  </section>
</body>
</html>
```